lantern productions business cards design

design a clean look but creative business card for a production company, I'm a freelance producer and launching my startup, would like to keep a clean professional look but still creative

Target Market(s)

businesses

Industry/Entity Type

video production

Contact Information for Business Card

logo, name (Mark Ellis), Title (Producer), (MFA Filmmaking, CSPT Los Angeles), contact number & email ID

Colors

Designer to choose only greyscale colors for use in the design.

Requirements
Must have
• logo, black and white colors, you can play with their shades
Nice to have
• a unique design, not necessarily a typical size card
Should not have
• too colorful or playful

```html
<!DOCTYPE html>
<html lang="en">
<head>
<meta charset="utf-8">
<title>Lantern Productions – Business Cards</title>
<link rel="stylesheet" href="https://fonts.googleapis.com/css2?family=Cinzel:wght@500&family=Arimo:wght@400&display=swap">
<style>
  :root {
    --stage: #2b2b2c;
    --card: #1b1c1e;
    --card-back-top: #2a2b2d;
    --card-back-bottom: #121314;
    --ink: #ffffff;
    --ink-soft: #e4e4e4;
    --ink-muted: #bdbdbd;
    --rule: #9a9a9a;
  }
  html, body {
    margin: 0;
    padding: 0;
    width: 1200px;
    height: 1108px;
    overflow: hidden;
    background: var(--stage);
  }
  .stage {
    position: relative;
    width: 1200px;
    height: 1108px;
    display: flex;
    justify-content: center;
    align-items: center;
    gap: 64px;
  }
  .card {
    position: relative;
    width: 440px;
    height: 700px;
    border-radius: 26px;
    background: var(--card);
    box-shadow: 0 10px 30px rgba(0,0,0,0.45);
    overflow: hidden;
  }
  .card-front {
    display: flex;
    flex-direction: column;
    align-items: center;
    color: var(--ink);
  }
  .brand {
    margin-top: 64px;
    display: flex;
    flex-direction: column;
    align-items: center;
    font-family: 'Cinzel', serif;
    font-weight: 500;
    color: var(--ink);
  }
  .brand-square {
    width: 18px;
    height: 18px;
    background: var(--ink);
    margin-bottom: 22px;
  }
  .brand-name {
    font-size: 58px;
    line-height: 1;
    letter-spacing: 1px;
  }
  .brand-sub {
    font-size: 26px;
    letter-spacing: 4px;
    margin-top: 6px;
  }
  .contact {
    margin-top: auto;
    margin-bottom: 64px;
    display: flex;
    flex-direction: column;
    align-items: center;
    text-align: center;
  }
  .person-name {
    font-family: 'Cinzel', serif;
    font-weight: 500;
    font-size: 34px;
    letter-spacing: 0.5px;
  }
  .person-title {
    font-family: 'Arimo', sans-serif;
    font-size: 19px;
    letter-spacing: 1.5px;
    color: var(--ink-soft);
    margin-top: 4px;
  }
  .person-credentials {
    font-family: 'Arimo', sans-serif;
    font-size: 15px;
    letter-spacing: 1.2px;
    color: var(--ink-muted);
    margin-top: 6px;
  }
  .divider {
    width: 150px;
    height: 1px;
    background: var(--rule);
    margin: 16px 0 14px;
  }
  .contact-line {
    font-family: 'Arimo', sans-serif;
    font-size: 22px;
    letter-spacing: 1px;
    color: var(--ink-soft);
    line-height: 1.35;
  }
  .card-back {
    background: linear-gradient(160deg, var(--card-back-top), var(--card-back-bottom));
  }
  .back-pattern {
    position: absolute;
    inset: 0;
  }
  .back-mark {
    position: absolute;
    right: 74px;
    bottom: 128px;
    font-family: 'Cinzel', serif;
    font-weight: 500;
    font-size: 22px;
    letter-spacing: 2px;
    color: var(--ink);
  }
</style>
</head>
<body>
  <main class="stage">
    <section class="card card-front">
      <div class="brand">
        <div class="brand-square"></div>
        <div class="brand-name">LANTERN</div>
        <div class="brand-sub">PRODUCTIONS</div>
      </div>
      <div class="contact">
        <div class="person-name">Mark Ellis</div>
        <div class="person-title">PRODUCER</div>
        <div class="person-credentials">MFA FILMMAKING, CSPT LOS ANGELES</div>
        <div class="divider"></div>
        <div class="contact-line">044-555 010 234</div>
        <div class="contact-line">HELLO@LANTERNPROD.COM</div>
      </div>
    </section>
    <section class="card card-back">
      <div class="back-pattern" role="img" aria-label="Repeating tonal pattern of the brand mark in glossy dark grey"></div>
      <div class="back-mark">LANTERN</div>
    </section>
  </main>
</body>
</html>
```